Interior Decorating and Event Styling Business Card Design

We need a business card design for a bespoke interior decorating and event styling business, mostly weddings. We also do custom paint finishes and painted floor finishes. We want something simple, organic and stylish with good colour tones used.

On our card we would like our services listed like so -

Interior Decorating
Wedding and Event Styling
Bespoke furniture paint finishes
Painted floor finishes

Industry/Entity Type

Paint

Contact Information for Business Card

Mabel & Moss Design
Rosalind 0487315026
Petra 0439572604
rosalind.carver@mailbrook.com.au
petraloom@tmv4.com.au

```html
<!DOCTYPE html>
<html lang="en">
<head>
<meta charset="utf-8">
<title>Mabel &amp; Moss Design — Business Card</title>
<link rel="stylesheet" href="https://fonts.googleapis.com/css2?family=EB+Garamond:ital,wght@0,400;0,500;1,400;1,500&display=swap">
<style>
  :root {
    --page-bg: #f1e2dc;
    --leaf-light: #80ad3d;
    --leaf-dark: #5e8a31;
    --glow: #e3f7b0;
    --wreath: #c9d7b6;
    --ink: #1f2a14;
    --ink-soft: #14200c;
    --flourish: #e8f0dc;
  }
  * { box-sizing: border-box; margin: 0; padding: 0; }
  html, body { width: 1200px; height: 1000px; overflow: hidden; }
  body {
    position: relative;
    background: var(--page-bg);
    font-family: "EB Garamond", Georgia, serif;
    color: var(--ink);
  }

  .card {
    position: absolute;
    width: 545px;
    border-radius: 16px;
    overflow: hidden;
    background: var(--leaf-light);
  }
  .card__band {
    position: absolute;
    left: 0; right: 0; bottom: 0;
    background: var(--leaf-dark);
  }
  .card__glow {
    position: absolute;
    border-radius: 50%;
    background: radial-gradient(ellipse at center, var(--glow) 0%, rgba(227,247,176,.55) 45%, rgba(227,247,176,0) 75%);
  }
  .wreath {
    position: absolute;
    border-radius: 50%;
    background: radial-gradient(ellipse at center, rgba(227,247,176,0) 55%, var(--wreath) 64%, #a9bf91 78%, rgba(169,191,145,0) 90%);
  }
  .brand-name {
    position: absolute;
    text-align: center;
    font-family: "EB Garamond", Georgia, serif;
    font-weight: 500;
    font-style: normal;
    color: var(--ink-soft);
    line-height: 1.05;
  }

  /* Front: services */
  .card--front { left: 67px; top: 527px; height: 305px; }
  .card--front .card__band { top: 160px; }
  .card--front .card__glow { left: 150px; top: 90px; width: 245px; height: 150px; }
  .card--front .wreath { left: 130px; top: 80px; width: 285px; height: 165px; }
  .card--front .brand-name { left: 160px; top: 122px; width: 225px; font-size: 30px; }

  .service {
    position: absolute;
    font-style: italic;
    font-size: 27px;
    line-height: 1.05;
    color: var(--ink);
    text-shadow: 0 1px 0 rgba(255,255,255,.35), 0 2px 3px rgba(0,0,0,.25);
  }
  .service--tl { left: 24px; top: 24px; }
  .service--tr { right: 24px; top: 24px; text-align: right; width: 250px; }
  .service--bl { left: 24px; top: 250px; }
  .service--br { right: 24px; top: 250px; text-align: right; }

  /* Back: contacts */
  .card--back { left: 565px; top: 128px; height: 325px; }
  .card--back .card__band { top: 182px; }
  .card--back .card__glow { left: 160px; top: 20px; width: 230px; height: 150px; }
  .card--back .wreath { left: 175px; top: 28px; width: 195px; height: 122px; }
  .card--back .brand-name { left: 190px; top: 62px; width: 165px; font-size: 23px; }

  .contact {
    position: absolute;
    top: 182px;
    font-size: 20px;
    line-height: 1.1;
    color: var(--ink);
    text-shadow: 0 1px 0 rgba(255,255,255,.25), 0 2px 2px rgba(0,0,0,.2);
  }
  .contact--left { left: 35px; width: 215px; }
  .contact--right { left: 345px; width: 190px; }
  .contact__name {
    text-align: center;
    font-size: 22px;
    margin-top: 6px;
  }
  .contact__flourish {
    display: block;
    margin: 2px auto 8px;
  }
  .contact__email-domain { text-align: right; }

  .centre-ornament {
    position: absolute;
    left: 222px; top: 190px;
  }
</style>
</head>
<body>

  <section class="card card--back" aria-label="Business card, contact side">
    <div class="card__band"></div>
    <div class="card__glow"></div>
    <div class="wreath" role="img" aria-label="Oval wreath of leaves and grapes framing the business name"></div>
    <div class="brand-name">Mabel &amp; Moss<br>Design</div>

    <div class="contact contact--left">
      <p class="contact__name">Rosalind</p>
      <svg class="contact__flourish" width="120" height="14" viewBox="0 0 120 14" role="img" aria-label="Small scroll flourish under the name">
        <rect x="0" y="5" width="120" height="4" rx="2" fill="var(--flourish)" opacity=".7"/>
      </svg>
      <p>Phone : 0487315026</p>
      <p>Mail : rosalind.carver</p>
      <p class="contact__email-domain">@mailbrook.com.au</p>
    </div>

    <svg class="centre-ornament" width="100" height="100" viewBox="0 0 100 100" role="img" aria-label="Decorative scrollwork medallion">
      <rect x="20" y="20" width="60" height="60" rx="8" transform="rotate(45 50 50)" fill="var(--flourish)" opacity=".45"/>
    </svg>

    <div class="contact contact--right">
      <p class="contact__name">Petra</p>
      <svg class="contact__flourish" width="120" height="14" viewBox="0 0 120 14" role="img" aria-label="Small scroll flourish under the name">
        <rect x="0" y="5" width="120" height="4" rx="2" fill="var(--flourish)" opacity=".7"/>
      </svg>
      <p>Phone : 0439572604</p>
      <p>Mail : petraloom</p>
      <p class="contact__email-domain">@tmv4.com.au</p>
    </div>
  </section>

  <section class="card card--front" aria-label="Business card, services side">
    <div class="card__band"></div>
    <div class="card__glow"></div>
    <div class="wreath" role="img" aria-label="Oval wreath of leaves and grapes framing the business name"></div>
    <div class="brand-name">Mabel &amp; Moss<br>Design</div>

    <p class="service service--tl">Interior Decorating</p>
    <p class="service service--tr">Bespoke furniture paint finishes</p>
    <p class="service service--bl">Wedding and Event Styling</p>
    <p class="service service--br">Painted floor finishes</p>
  </section>

</body>
</html>
```